stationary for a modern hotel
Venmiro Hotels
Project: stationary for a modern hotel
stationary for a modern hotel - Hospitality Industry
Creative Brief
Use same font as used in my logo
anything that can go very well with my logo
Simple
Tundeyemi Okafordike
G.M
Venmiro Hotels Plot 318,Adebanjo-Ekwueme Way,Garki District Abuja Nigeria
tunde@venmirohotels.com
www.venmirohotels.com

```html
<!DOCTYPE html>
<html lang="en">
<head>
<meta charset="utf-8">
<title>Venmiro Hotels Stationery</title>
<link href="https://fonts.googleapis.com/css2?family=Cinzel:wght@500&family=Open+Sans:wght@400;600&display=swap" rel="stylesheet">
<style>
:root{
  --stage:#e9e4dc;
  --paper:#ffffff;
  --brown-dark:#5a3a1e;
  --brown:#7a5331;
  --tan:#a8845d;
  --tan-light:#c9ad8a;
  --ink:#4a3a2c;
  --rule:#c8beb2;
  --label:#3b2a1c;
}
*{margin:0;padding:0;box-sizing:border-box}
html,body{width:1200px;height:674px;overflow:hidden;background:var(--stage)}
body{position:relative;font-family:"Open Sans",sans-serif;color:var(--ink)}
.piece{position:absolute;background:var(--paper);box-shadow:0 2px 6px rgba(0,0,0,.18);overflow:hidden}
.piece-label{position:absolute;font-size:7px;font-weight:600;color:var(--label);text-align:center;white-space:nowrap}
.brand{font-family:"Cinzel",serif;font-weight:500;letter-spacing:.06em;color:var(--brown);white-space:nowrap}
.brand-light{color:#f3e8da}
.swoosh{position:absolute;inset:0;width:100%;height:100%}
.center{position:absolute;left:0;right:0;text-align:center}

/* business cards */
.card{width:134px;height:78px;top:48px}
.card-front .brand{position:absolute;left:10px;top:12px;font-size:9px}
.card-front .person{position:absolute;right:10px;top:40px;text-align:right;font-size:5px;line-height:1.4}
.card-front .person strong{font-size:6px;color:var(--brown)}
.card-front .contact{position:absolute;left:10px;bottom:8px;font-size:4px;line-height:1.4}
.card-back .brand{top:32px;font-size:10px}
.card-dark{background:var(--brown-dark)}
.card-tan{background:var(--tan)}

/* envelope front */
.envelope-front{left:785px;top:48px;width:391px;height:115px}
.envelope-front .brand{position:absolute;left:16px;top:14px;font-size:11px}
.envelope-front .return{position:absolute;left:16px;top:32px;font-size:5px;line-height:1.4}

/* sheets */
.sheet{top:163px;width:355px;height:497px}
.fax{left:29px}
.letterhead{left:403px;width:360px}
.sheet .brand-top{top:22px;font-size:13px}
.watermark{top:295px;font-family:"Cinzel",serif;font-size:32px;letter-spacing:.06em;color:var(--brown);opacity:.07}
.footer{bottom:14px;font-size:5px;line-height:1.5}
.footer strong{font-size:6px;color:var(--brown)}
.fax-title{position:absolute;right:30px;top:66px;font-size:9px;font-weight:600;color:var(--brown)}
.fax-table{position:absolute;left:60px;top:82px;width:270px;border-collapse:collapse;font-size:6px}
.fax-table td{border:1px solid var(--rule);height:15px;padding:0 4px}
.fax-table .field{width:40px;color:var(--brown)}
.checks{position:absolute;left:60px;top:158px;display:flex;gap:14px;font-size:5px}
.checks span::before{content:"";display:inline-block;width:5px;height:5px;border:1px solid var(--tan);margin-right:3px;vertical-align:-1px}

/* envelope backs */
.envelope-back{left:792px;width:384px}
.back-1{top:283px;height:125px}
.back-2{top:439px;height:104px}
.back-3{top:566px;height:94px}
.envelope-back .brand{position:absolute;left:0;right:0;text-align:center;font-size:10px}
</style>
</head>
<body>

<!-- business cards -->
<div class="piece-label" style="left:29px;top:34px;width:134px">Business Card (Front)</div>
<div class="piece card card-front" style="left:29px">
  <svg class="swoosh" viewBox="0 0 134 78" preserveAspectRatio="none"><path d="M134 48 C110 60 90 70 70 78 H134 Z" fill="var(--tan)"/></svg>
  <div class="brand">Venmiro Hotels</div>
  <div class="person"><strong>Tundeyemi Okafordike</strong><br>G.M</div>
  <div class="contact">Plot 318,Adebanjo-Ekwueme Way,Garki District, Abuja<br>tunde@venmirohotels.com · www.venmirohotels.com</div>
</div>

<div class="piece-label" style="left:281px;top:34px;width:134px">Business Card (Back) Option 1</div>
<div class="piece card card-back" style="left:281px"><div class="center brand">Venmiro Hotels</div></div>

<div class="piece-label" style="left:432px;top:34px;width:134px">Business Card (Back) Option 2</div>
<div class="piece card card-back card-dark" style="left:432px"><div class="center brand brand-light">Venmiro Hotels</div></div>

<div class="piece-label" style="left:576px;top:34px;width:134px">Business Card (Back) Option 3</div>
<div class="piece card card-back card-tan" style="left:576px"><div class="center brand brand-light">Venmiro Hotels</div></div>

<!-- envelope front -->
<div class="piece-label" style="left:785px;top:34px;width:391px">Envelope (Front)</div>
<div class="piece envelope-front">
  <div class="brand">Venmiro Hotels</div>
  <div class="return">Plot 318,Adebanjo-Ekwueme Way,Garki District<br>Abuja, Nigeria</div>
</div>

<!-- fax cover -->
<div class="piece-label" style="left:29px;top:151px;width:355px">Fax Cover</div>
<div class="piece sheet fax">
  <svg class="swoosh" viewBox="0 0 355 497" preserveAspectRatio="none">
    <path d="M0 0 H60 C28 70 12 170 0 270 Z" fill="var(--brown)"/>
    <path d="M0 0 H40 C18 60 6 150 0 220 Z" fill="var(--tan)"/>
    <path d="M355 497 V320 C345 410 310 470 250 497 Z" fill="var(--brown)"/>
  </svg>
  <div class="center brand brand-top">Venmiro Hotels</div>
  <div class="fax-title">FAX</div>
  <table class="fax-table">
    <tr><td class="field">To:</td><td></td><td class="field">From:</td><td></td></tr>
    <tr><td class="field">Fax:</td><td></td><td class="field">Pages:</td><td></td></tr>
    <tr><td class="field">Phone:</td><td></td><td class="field">Date:</td><td></td></tr>
    <tr><td class="field">Re:</td><td></td><td class="field">Cc:</td><td></td></tr>
  </table>
  <div class="checks"><span>Urgent</span><span>For Review</span><span>Please Comment</span><span>Please Reply</span><span>Please Recycle</span></div>
  <div class="center watermark">VENMIRO HOTELS</div>
  <div class="center footer"><strong>Venmiro Hotels</strong><br>Plot 318,Adebanjo-Ekwueme Way,Garki District, Abuja Nigeria<br>+234 (0)9 555 0182 · tunde@venmirohotels.com · www.venmirohotels.com</div>
</div>

<!-- letterhead -->
<div class="piece-label" style="left:403px;top:151px;width:360px">Letterhead</div>
<div class="piece sheet letterhead">
  <svg class="swoosh" viewBox="0 0 360 497" preserveAspectRatio="none">
    <path d="M0 0 H60 C28 70 12 170 0 270 Z" fill="var(--brown)"/>
    <path d="M0 0 H40 C18 60 6 150 0 220 Z" fill="var(--tan)"/>
    <path d="M360 497 V320 C350 410 315 470 255 497 Z" fill="var(--brown)"/>
  </svg>
  <div class="center brand brand-top">Venmiro Hotels</div>
  <div class="center watermark">VENMIRO HOTELS</div>
  <div class="center footer"><strong>Venmiro Hotels</strong><br>Plot 318,Adebanjo-Ekwueme Way,Garki District, Abuja Nigeria<br>+234 (0)9 555 0182 · info@venmirohotels.com · www.venmirohotels.com</div>
</div>

<!-- envelope backs -->
<div class="piece-label" style="left:792px;top:271px;width:384px">Envelope (Back) Option 1</div>
<div class="piece envelope-back back-1">
  <svg class="swoosh" viewBox="0 0 384 125" preserveAspectRatio="none">
    <path d="M0 0 H384 L200 70 Q192 74 184 70 Z" fill="#fff" stroke="var(--tan)" stroke-width="1.5"/>
    <path d="M0 125 L170 60 M384 125 L214 60" stroke="var(--rule)" stroke-width="1"/>
  </svg>
  <div class="brand" style="top:22px">Venmiro Hotels</div>
</div>

<div class="piece-label" style="left:792px;top:427px;width:384px">Envelope (Back) Option 2</div>
<div class="piece envelope-back back-2">
  <svg class="swoosh" viewBox="0 0 384 104" preserveAspectRatio="none">
    <path d="M0 0 H384 L200 62 Q192 66 184 62 Z" fill="var(--brown-dark)"/>
    <path d="M0 104 L165 52 M384 104 L219 52" stroke="var(--rule)" stroke-width="1"/>
  </svg>
  <div class="brand brand-light" style="top:18px">Venmiro Hotels</div>
</div>

<div class="piece-label" style="left:792px;top:554px;width:384px">Envelope (Back) Option 3</div>
<div class="piece envelope-back back-3">
  <svg class="swoosh" viewBox="0 0 384 94" preserveAspectRatio="none">
    <path d="M0 0 H384 L200 58 Q192 62 184 58 Z" fill="var(--tan)"/>
    <path d="M0 94 L165 48 M384 94 L219 48" stroke="var(--rule)" stroke-width="1"/>
  </svg>
  <div class="brand brand-light" style="top:16px">Venmiro Hotels</div>
</div>

</body>
</html>
```